Australian Software Consultancy needs new Business Card Design

Design Business Card based on existing design artefacts (attached). We are open to all designs. As its a 2 sided design and we thought it might be quite striking to have one side with a black background and te other side with a white background.

Target Market(s)

Financial Services mainly.

Industry/Entity Type

Business

Contact Information for Business Card

Name :
Position :
Email :

Requirements
Must have
• Funky design using our existing assets

```html
<!DOCTYPE html>
<html lang="en">
<head>
<meta charset="utf-8">
<title>Northlane Business Card</title>
<link rel="stylesheet" href="https://fonts.googleapis.com/css2?family=Quicksand:wght@500;700&display=swap">
<style>
  :root {
    --page: #e6e6e6;
    --card-black: #000000;
    --card-white: #ffffff;
    --accent-red: #e31e24;
    --text-dark: #1a1a1a;
    --text-light: #ffffff;
  }
  * { box-sizing: border-box; margin: 0; padding: 0; }
  html, body {
    width: 1200px;
    height: 1200px;
    overflow: hidden;
    background: var(--page);
    font-family: "Quicksand", sans-serif;
  }
  .sheet {
    width: 1200px;
    height: 1200px;
    display: flex;
    flex-direction: column;
    align-items: center;
    justify-content: center;
    gap: 60px;
  }
  .card {
    position: relative;
    width: 840px;
    height: 480px;
    background: var(--card-black);
    overflow: hidden;
    box-shadow: 0 10px 28px rgba(0,0,0,0.25);
  }
  .brand-name {
    position: absolute;
    left: 0;
    right: 0;
    text-align: center;
    color: var(--text-light);
    font-weight: 700;
    letter-spacing: 1px;
    text-transform: uppercase;
    line-height: 1;
  }
  /* front side */
  .card--front .brand-name {
    top: 120px;
    font-size: 32px;
  }
  .white-arc {
    position: absolute;
    inset: 0;
    width: 840px;
    height: 480px;
  }
  .white-arc .arc-fill { fill: var(--card-white); }
  .white-arc .arc-edge { fill: none; stroke: var(--accent-red); stroke-width: 5; }
  .contact {
    position: absolute;
    left: 0;
    right: 0;
    top: 285px;
    text-align: center;
    color: var(--text-dark);
  }
  .contact-name {
    color: var(--accent-red);
    font-size: 40px;
    font-weight: 700;
    letter-spacing: 0.5px;
    line-height: 1.1;
  }
  .contact-position {
    margin-top: 8px;
    font-size: 18px;
    font-weight: 500;
    letter-spacing: 1px;
  }
  .contact-email {
    margin-top: 40px;
    font-size: 19px;
    font-weight: 500;
  }
  /* back side */
  .card--back .brand-name {
    top: 50%;
    transform: translateY(-50%);
    font-size: 46px;
  }
</style>
</head>
<body>
  <main class="sheet">
    <section class="card card--front" aria-label="Business card, front">
      <p class="brand-name">Northlane</p>
      <svg class="white-arc" viewBox="0 0 840 480" aria-hidden="true">
        <path class="arc-fill" d="M0 480 V470 C150 300 420 200 840 210 V480 Z"/>
        <path class="arc-edge" d="M0 470 C150 300 420 200 840 210"/>
      </svg>
      <div class="contact">
        <p class="contact-name">NAME TITLE</p>
        <p class="contact-position">POSITION</p>
        <p class="contact-email">Email : hello@northlane.dev</p>
      </div>
    </section>

    <section class="card card--back" aria-label="Business card, back">
      <p class="brand-name">Northlane</p>
    </section>
  </main>
</body>
</html>
```